Business card and company stationary - Corvane Cleaning Ltd

1. Who are we and who are our customers?

o We are a relatively new cleaning company, established December 2008. We are a small company. We have 24 staff and we offer domestic and commercial cleaning services.
o We both (me and my wife) have been working for many years in the cleaning industry. We worked for some of the biggest and best cleaning companies in UK. We’ve been operatives, supervisors and managers.
o Inevitably after so many years of working for someone else, we decided to start our own business.
o Our domestic customers are middle class families and busy professionals. We’ve got some commercial customers, mainly offices.
o We are growing steadily.

2. What do we do? What are our services?

o Cleaning. We’ve got range of services - not to many but still can be daunting and confusing for some.
o Generally we’ve got domestic and commercial clients. The approach to the domestic cleaning customers is different to the commercial. In the way we want to say that it is cleaning that we do, but we acknowledge the environment and we appreciate the personal circumstances and requirements that are present. We do care, we listen and we try to work out the best possible way to complete our work.
o Mainly we get our work through referrals

3. What do we want with our stationery ?

o To place and maintain our message and reach out to people and organisations
o We want to advertise, communicate and sale.
o We are going to sell services.
o Increase membership, loyalty and support.

We are after business card design, headed letter and compliment slip.
We would like the headed letter to be created in formats suitable for :
- printing format
- also for use in our daily correspondence via e mail with clients and staff in a easy to edit and write format

The website we have is still under contraction and the domain is corvanecleaning.example

Target Market(s)

Families, individuals, businesses.

Industry/Entity Type

Cleaning Service

Contact Information for Business Card

FRONT :
Company Name - Corvane Cleaning Ltd
Company address - 41 Pelbury Rd, Pelbury, Essex, RM14 7QT
Name - Mrs. Teodora Vasilkova - Tedi
Title - Managing Director
Company phone - 020 8837 2591
E mail - tedi.vasilkova@corvanecleaning.example

BACK :

Company website - corvanecleaning.example
E mail - enquiries@corvanecleaning.example

Font styles to use
Serif

Requirements
Must have
• The above items and company logo...maybe at the back. But I'm free for any suggestions.

```html
<!DOCTYPE html>
<html lang="en">
<head>
<meta charset="utf-8">
<title>Corvane Cleaning Ltd – Business Card</title>
<link rel="stylesheet" href="https://fonts.googleapis.com/css2?family=Source+Serif+4:opsz,wght@8..60,400;8..60,600;8..60,700&display=swap">
<style>
  :root {
    --page-bg: #d9d9d6;
    --card-bg: #e6e7e7;
    --band-dark: #2f3031;
    --panel-grey: #9c9d9e;
    --panel-light: #acadae;
    --ink: #2b2c2d;
    --white: #ffffff;
    --divider: #55575a;
    --mark-teal: #35b4cf;
  }
  * { box-sizing: border-box; margin: 0; padding: 0; }
  html, body {
    width: 1200px; height: 1200px; overflow: hidden;
    background: var(--page-bg);
    font-family: "Source Serif 4", Georgia, serif;
  }
  .canvas { position: relative; width: 1200px; height: 1200px; }
  .card {
    position: absolute; left: 150px; width: 900px; height: 514px;
    background: var(--card-bg); overflow: hidden;
    box-shadow: 0 6px 18px rgba(0,0,0,0.18);
  }
  .card--back { top: 56px; }
  .card--front { top: 630px; }
  .card-shapes { position: absolute; inset: 0; width: 900px; height: 514px; }

  .brand { position: absolute; display: flex; align-items: center; gap: 18px; }
  .brand-dot {
    width: 58px; height: 58px; border-radius: 50%;
    background: var(--mark-teal); flex: none;
  }
  .brand-name {
    color: var(--ink); font-weight: 600; font-size: 38px;
    line-height: 1.08; letter-spacing: 4px; text-transform: uppercase;
  }
  .card--back .brand { left: 260px; top: 150px; }
  .card--front .brand { left: 50px; top: 120px; }

  .web-band-url {
    position: absolute; left: 0; right: 0; top: 382px; height: 70px;
    display: flex; align-items: center; justify-content: center;
    padding-left: 180px;
    color: var(--white); font-weight: 600; font-size: 24px; letter-spacing: 0.3px;
  }

  .services { position: absolute; left: 0; top: 300px; height: 72px; width: 470px; }
  .service {
    position: absolute; top: 0; height: 72px; display: flex; align-items: center;
    color: var(--white); font-size: 12px; letter-spacing: 1px; text-transform: uppercase;
  }
  .service--cleaning { left: 28px; }
  .service--housekeeping { left: 168px; }
  .service--support { left: 312px; }

  .contact { position: absolute; left: 550px; top: 130px; width: 330px; color: var(--white); }
  .contact-name { font-weight: 700; font-size: 22px; line-height: 1.2; }
  .contact-title { font-size: 16px; margin-top: 4px; }
  .contact-list { list-style: none; margin-top: 34px; }
  .contact-item { display: flex; align-items: flex-start; gap: 14px; font-size: 14px; line-height: 1.35; margin-bottom: 20px; }
  .contact-icon { width: 16px; height: 16px; flex: none; margin-top: 2px; }
</style>
</head>
<body>
<div class="canvas">

  <section class="card card--back" aria-label="Business card back">
    <svg class="card-shapes" viewBox="0 0 900 514" aria-hidden="true">
      <rect x="0" y="382" width="900" height="70" fill="var(--band-dark)"/>
    </svg>
    <div class="brand">
      <span class="brand-dot"></span>
      <span class="brand-name">Corvane<br>Cleaning Ltd</span>
    </div>
    <div class="web-band-url">www.corvanecleaning.example</div>
  </section>

  <section class="card card--front" aria-label="Business card front">
    <svg class="card-shapes" viewBox="0 0 900 514" aria-hidden="true">
      <polygon points="640,0 900,0 900,514 330,514" fill="var(--panel-grey)"/>
      <polygon points="640,0 730,0 440,514 330,514" fill="var(--panel-light)"/>
      <polygon points="0,300 480,300 440,372 0,372" fill="var(--band-dark)"/>
      <line x1="150" y1="300" x2="142" y2="372" stroke="var(--divider)" stroke-width="1.5"/>
      <line x1="298" y1="300" x2="290" y2="372" stroke="var(--divider)" stroke-width="1.5"/>
    </svg>

    <div class="brand">
      <span class="brand-dot"></span>
      <span class="brand-name">Corvane<br>Cleaning Ltd</span>
    </div>

    <div class="services">
      <span class="service service--cleaning">Cleaning</span>
      <span class="service service--housekeeping">House Keeping</span>
      <span class="service service--support">Support Services</span>
    </div>

    <div class="contact">
      <p class="contact-name">Mrs. Teodora Vasilkova - Tedi</p>
      <p class="contact-title">Managing Director</p>
      <ul class="contact-list">
        <li class="contact-item">
          <svg class="contact-icon" viewBox="0 0 18 18" aria-hidden="true"><path d="M9 2 L17 9 H14.5 V16 H10.5 V11.5 H7.5 V16 H3.5 V9 H1 Z" fill="var(--white)"/></svg>
          <span>41 Pelbury Rd,<br>Pelbury, Essex, RM14 7QT</span>
        </li>
        <li class="contact-item">
          <svg class="contact-icon" viewBox="0 0 18 18" aria-hidden="true"><path d="M4 1.5 L7 5 L5.5 7 C6.5 9 9 11.5 11 12.5 L13 11 L16.5 14 L14.5 16.5 C8 16 2 10 1.5 3.5 Z" fill="var(--white)"/></svg>
          <span>020 8837 2591</span>
        </li>
        <li class="contact-item">
          <svg class="contact-icon" viewBox="0 0 18 18" aria-hidden="true"><rect x="1.5" y="4" width="15" height="10.5" rx="1" fill="var(--white)"/><path d="M1.5 4.5 L9 10 L16.5 4.5" fill="none" stroke="var(--panel-grey)" stroke-width="1.4"/></svg>
          <span>tedi.vasilkova@corvanecleaning.example</span>
        </li>
        <li class="contact-item">
          <svg class="contact-icon" viewBox="0 0 18 18" aria-hidden="true"><circle cx="9" cy="9" r="7.5" fill="var(--white)"/><g fill="none" stroke="var(--panel-grey)" stroke-width="1.1"><ellipse cx="9" cy="9" rx="3.2" ry="7.5"/><line x1="1.5" y1="9" x2="16.5" y2="9"/><line x1="3" y1="5" x2="15" y2="5"/><line x1="3" y1="13" x2="15" y2="13"/></g></svg>
          <span>www.corvanecleaning.example</span>
        </li>
      </ul>
    </div>
  </section>

</div>
</body>
</html>
```